MS word document templates for consultancy

I need the following templates for my business using my logo as branding.

- General report template
- Letter head template
- Tender proposal template

The templates should be sleek and with minimal colors, but with a small amount of green and grey where appropriate (as per attached logo and email signature). Font should be consistent with the text in the email signature.

```html
<!DOCTYPE html>
<html lang="en">
<head>
<meta charset="utf-8">
<title>Brightpath Group Letterhead</title>
<link rel="stylesheet" href="https://fonts.googleapis.com/css2?family=Montserrat:wght@400;500;700&display=swap">
<style>
  :root {
    --brand-green: #2a9346;
    --ink: #000000;
    --paper: #ffffff;
  }
  html, body {
    margin: 0;
    padding: 0;
    overflow: hidden;
    background: var(--paper);
  }
  .letterhead {
    position: relative;
    width: 848px;
    height: 1200px;
    background: var(--paper);
    overflow: hidden;
    font-family: "Montserrat", sans-serif;
  }
  .shapes {
    position: absolute;
    inset: 0;
  }
  .brand-name {
    position: absolute;
    left: 88px;
    top: 96px;
    margin: 0;
    font-size: 35px;
    font-weight: 400;
    letter-spacing: 0.5px;
    color: var(--paper);
    white-space: nowrap;
  }
  .sender {
    position: absolute;
    right: 85px;
    top: 114px;
    text-align: right;
    color: var(--paper);
    line-height: 23px;
  }
  .sender-name {
    font-size: 19.5px;
    font-weight: 700;
    display: block;
  }
  .sender-role {
    font-size: 19.5px;
    font-weight: 500;
    display: block;
  }
  .contact-phone {
    position: absolute;
    left: 85px;
    top: 1111px;
    display: flex;
    align-items: center;
    gap: 11px;
    color: var(--paper);
    font-size: 19px;
    font-weight: 500;
  }
  .contact-phone svg {
    display: block;
  }
</style>
</head>
<body>
<div class="letterhead">
  <svg class="shapes" width="848" height="1200" viewBox="0 0 848 1200" aria-hidden="true">
    <!-- header -->
    <polyline points="509,99 518,72 848,72" fill="none" stroke="var(--ink)" stroke-width="2.5"/>
    <polygon points="484,100 848,100 848,175 458,175" fill="var(--brand-green)"/>
    <polygon points="0,58 497,58 450,199 0,199" fill="var(--ink)"/>
    <polygon points="0,176 157,176 140,225 0,225" fill="var(--brand-green)"/>
    <!-- footer -->
    <polygon points="0,1099 627,1099 609,1152 0,1152" fill="var(--brand-green)"/>
    <polyline points="0,1165 256,1165 260,1152" fill="none" stroke="var(--ink)" stroke-width="2.5"/>
    <polygon points="704,1049 848,1049 848,1098 688,1098" fill="var(--brand-green)"/>
    <polygon points="637,1070 697,1070 688,1098 848,1098 848,1178 601,1178" fill="var(--ink)"/>
  </svg>

  <p class="brand-name">Brightpath Group</p>

  <div class="sender">
    <span class="sender-name">Daniel Rourke</span>
    <span class="sender-role">Managing Director</span>
  </div>

  <div class="contact-phone">
    <svg width="30" height="30" viewBox="0 0 30 30" aria-hidden="true">
      <circle cx="15" cy="15" r="15" fill="var(--paper)"/>
      <path d="M10.2 7.5c.6-.4 1.3-.3 1.7.3l1.7 2.6c.4.6.3 1.3-.2 1.7l-1 .8c.7 1.7 2 3.1 3.7 3.9l.8-1c.4-.5 1.2-.6 1.7-.2l2.6 1.7c.6.4.7 1.2.3 1.7l-1 1.4c-.6.8-1.6 1.1-2.6.8-4.2-1.3-7.4-4.6-8.7-8.8-.3-1 0-2 .8-2.6z" fill="var(--brand-green)"/>
    </svg>
    <span class="phone-number">0400 555 318</span>
  </div>
</div>
</body>
</html>
```